Bluewater Getaways KT needs a new Website

We have an old website that is just that - old. We need a fresh website that is professional graphic designed that has the following features.
1. Can be updated by ourselves in some areas.
2. Has a shopping cart.
3. Has links to download PDF files
4. Has links to other pages in the website
5. Includes social media links
6. Has a client log-in area
Full details in brief provided.

SORRY BUT IT'S URGENT. We've taken too long to write the details and it is now urgent. So my apologies I will be asking for designers to work quickly.

We will continue to use our existing web hosting company and url. Their is a link to the old website in the Design Brief.
Updates

UPDATE:  Please see the new file UPDATE TO DESIGN BRIEF.
Thanks for all your submissions to date.  We hope the update will assist with your designs.
As indicated in previous messages, we are happy with the Home Page + 1 Page in order to select the designer to work with in creating the full design. 

Thankyou Designers.  Much appreciate your efforts.
It's getting late here on Norfolk so I won't have much chance too review any more designs this evening.
But for your information:
Designer 7318405 Ravindra Mehta is so far the closest to what we are seeking.
Thanks again. 

Reason: Have extended to Monday 7 October to give time for designers to submit after feedback today. Especially given the time differences

Target Market(s)

Very wide audience. Current client group not that tech savvy, but we hope to broaden our market and sell more creative products, and so website needs to consider how people now use media, ie tablets & iphones.

Industry/Entity Type

Shopping

Requirements
Nice to have
• PLEASE SEE THE "UPDATE TO THE DESIGN BRIEF"

```html
<!DOCTYPE html>
<html lang="en">
<head>
<meta charset="utf-8">
<title>Bluewater Getaways KT</title>
<link href="https://fonts.googleapis.com/css2?family=Arimo:wght@400;700&display=swap" rel="stylesheet">
<style>
:root{
  --orange:#f5821f;
  --orange-dark:#e8701a;
  --green:#1f9a3e;
  --text:#333;
  --muted:#666;
  --rule:#d6d6d6;
  --white:#fff;
  --link:#e8701a;
  --nav-active:#d9343f;
}
*{box-sizing:border-box;margin:0;padding:0}
html,body{width:865px;height:1200px;overflow:hidden}
body{background:var(--orange);font-family:"Arimo",Arial,sans-serif;color:var(--text);position:relative}
.panel{position:absolute;background:var(--white);border-radius:4px;overflow:hidden}
.site-header{left:69px;top:11px;width:725px;height:81px}
.brand{position:absolute;left:22px;top:22px;display:flex;align-items:center;gap:9px}
.brand-dot{width:30px;height:30px;border-radius:50%;background:var(--orange)}
.brand-name{font-size:15px;font-weight:700;color:var(--orange);line-height:1.05;width:120px}
.header-art{position:absolute;right:0;top:0;width:360px;height:100%;background:linear-gradient(90deg,rgba(255,255,255,1) 0%,#fbe7a6 35%,#f7c548 65%,#f08a24 100%)}
.main-nav{position:absolute;left:69px;top:95px;width:725px;height:27px;background:linear-gradient(#fff,#e6e6e6);border-radius:3px 3px 0 0;display:flex;align-items:center;padding-left:34px;gap:24px}
.main-nav a{font-size:9.5px;font-weight:700;color:#222;text-decoration:none;letter-spacing:.2px}
.main-nav a.is-highlight{color:var(--nav-active)}
.hero{position:absolute;left:69px;top:122px;width:725px;height:139px;background:linear-gradient(180deg,#6c8fb8 0%,#3f6a3c 38%,#4f7f3c 55%,#9fd6cf 72%,#e9dcc0 100%)}
.content{left:69px;top:269px;width:504px;height:833px;padding:24px 43px 0 43px}
.content h1{font-size:13px;font-weight:700;color:var(--green);margin:0 0 12px}
.content p{font-size:9.6px;line-height:12.4px;margin-bottom:12px;color:#2d2d2d}
.content a{color:var(--link);font-weight:700}
.badges{position:absolute;left:45px;top:512px;display:flex;gap:26px;align-items:center}
.badge{width:90px;height:56px;display:flex;align-items:center;justify-content:center}
.sidebar{left:582px;top:269px;width:212px;height:833px}
.side-block{padding:14px 14px 12px;border-bottom:1px solid #f4c9a2}
.side-block h2{font-size:9px;font-weight:700;color:#222;margin-bottom:10px;letter-spacing:.2px}
.contact{font-size:9px;line-height:12.5px;color:var(--muted);padding-left:17px}
.contact hr{border:0;border-top:1px dotted #aaa;margin:5px 0}
.contact strong{color:#222}
.contact a{color:var(--link);text-decoration:none;display:block}
.video{width:188px;height:105px;margin-left:-2px;background:linear-gradient(180deg,#2a64b3 0%,#4ea2dc 60%,#e7ddb9 100%);position:relative}
.video-bar{position:absolute;left:0;right:0;bottom:0;height:11px;background:#1a1a1a}
.video-caption{font-size:8.6px;line-height:11px;color:#333;margin-top:8px;position:relative;padding-right:24px}
.video-caption strong{display:block;font-size:9px}
.video-caption a{color:var(--link);text-decoration:none}
.video-caption svg{position:absolute;right:4px;top:18px}
.login-row{display:flex;align-items:center;gap:10px}
.field{width:138px;height:25px;border:1px solid #ccc;border-radius:2px;font-size:9.5px;color:#444;padding:7px 13px;margin-bottom:5px}
.promo{width:158px;height:99px;border-radius:3px;background:linear-gradient(180deg,#1d6bb0 0%,#5b9fd6 55%,#cfe3f2 80%,#7a6a55 100%);padding:7px 6px;color:#fff}
.promo b{display:block;font-size:12.5px;line-height:13px}
.promo span{font-size:8.4px}
.site-footer{left:69px;top:1108px;width:725px;height:80px}
.footer-brand{position:absolute;left:17px;top:14px;display:flex;align-items:center;gap:7px}
.footer-brand .brand-dot{width:22px;height:22px}
.footer-brand .brand-name{font-size:11px;width:90px}
.legal{position:absolute;left:18px;top:52px;font-size:8.6px;line-height:11px;color:#888}
.legal a{color:#888;text-decoration:none}
.footer-art{position:absolute;right:0;top:0;width:330px;height:100%;background:linear-gradient(90deg,rgba(255,255,255,1) 0%,#fbe7a6 35%,#f7c548 65%,#f08a24 100%)}
</style>
</head>
<body>
<header class="panel site-header">
  <div class="brand"><span class="brand-dot"></span><span class="brand-name">Bluewater Getaways KT</span></div>
  <div class="header-art" role="img" aria-label="Bright orange and yellow flower artwork"></div>
</header>
<nav class="main-nav">
  <a href="#">HOME</a><a href="#">OVERVIEW</a><a href="#">KESTREL TERN ISLAND SERVICES</a><a href="#">OUR SHOP</a><a href="#" class="is-highlight">MAKE A BOOKING</a><a href="#">TESTIMONIALS</a>
</nav>
<div class="hero" role="img" aria-label="Island beach with tall pine trees and a couple walking on the sand"></div>

<main class="panel content">
  <h1>WELCOME TO BLUEWATER GETAWAYS</h1>
  <p>Bluewater Getaways commenced trading in 2001 in Queensland Australia as Coral Coast Assisted Travel.</p>
  <p>Our services are based on the Disability Sector Quality System as defined in the Disability Services Act 2006 and subsequent amendments.</p>
  <p>We work closely with service users across government and non-government sectors in Australia, including the QLD, NSW and VIC State Government (Disability) Departments and Government Financial Trustees.</p>
  <p>We continually monitor and update our Risk Management procedures and have policies in place for the protection of our clients and staff. They include Liability Insurances, Workers Compensation and Travel Insurances. Contingency planning is an important and vital aspect of our operation.<br>Download the contents of our <a href="#">Policies &amp;Procedures</a>, <a href="#">Privacy Policy</a> and <a href="#">Complaints Procedure</a>.</p>
  <p>Our services double as a very positive form of respite and we have brokerage agreements in place with Carer Respite Centres in Australia.</p>
  <p>We maintain a Quality Framework and keep informed of the issues surrounding disability care through our membership with National Access Services and we keep in touch with the latest news from Access Care Network.</p>
  <p>We don't access any funding or donations. We invite support to assist in maintaining affordable programs for people with disabilities. CLICK here for details of how you can help.</p>
  <p>Our experience in travel for people with disabilities is extensive. We are presently undergoing accreditation in the National Travel Accreditation Scheme; once complete we will be entitled to use the Australian Federal Governments Q-MARK brands (below) which is theassurance that Bluewater Getaways KT is committed to professionalism both in business operations and delivery of service.</p>
  <div class="badges">
    <div class="badge"><svg width="80" height="46"><rect x="2" y="4" width="76" height="38" rx="3" fill="#222"/></svg></div>
    <div class="badge"><svg width="64" height="56"><rect x="2" y="2" width="60" height="52" rx="3" fill="#2f5f8f"/></svg></div>
    <div class="badge"><svg width="56" height="56"><circle cx="28" cy="28" r="26" fill="#1f8a3a"/></svg></div>
    <div class="badge"><svg width="84" height="50"><rect x="2" y="4" width="80" height="42" rx="3" fill="#f0a23a"/></svg></div>
  </div>
</main>

<aside class="panel sidebar">
  <section class="side-block">
    <h2>LOCATION &amp; CONTACTS</h2>
    <div class="contact">
      Marlin Lane, Pine Hollow<br>PO Box 514<br>Kestrel Tern Island NSW 2877<br>SOUTH PACIFIC<br>N.B.N. 315 062 418
      <hr>
      <strong>Telephone</strong><br>International + 67 23 51947<br>Australia 1800 463 218<br>New Zealand
      <hr>
      <a href="#">hello@bluewatergetaways.org</a><a href="#">www.bluewatergetaways.org</a><a href="#">www.friendbook.com/bluewatergetaways</a>
    </div>
  </section>
  <section class="side-block">
    <h2>IMAGES &amp; VIDEO</h2>
    <div class="video" role="img" aria-label="Video still of a tropical beach with palm tree and title lettering"><div class="video-bar"></div></div>
    <div class="video-caption"><strong>BLUEWATER VIDEO</strong>to see more photographs and video's LIKE our <a href="#">FRIENDBOOK</a> page
      <svg width="14" height="13" viewBox="0 0 14 13"><path d="M1 6h3v7H1zM5 6l3-6c1.5 0 2 1 1.7 2.3L9.3 5H13c.8 0 1.2.7 1 1.4l-1.3 5.4c-.2.7-.7 1.2-1.4 1.2H5z" fill="#3b6fc4"/></svg>
    </div>
  </section>
  <section class="side-block">
    <h2>CLIENT LOGIN</h2>
    <div class="field">Username</div>
    <div class="login-row"><div class="field">Password</div>
      <svg width="18" height="18"><circle cx="9" cy="9" r="9" fill="var(--orange)"/><path d="M7 5l4 4-4 4" stroke="#fff" stroke-width="2" fill="none"/></svg>
    </div>
  </section>
  <section class="side-block">
    <h2>SUPPORT US</h2>
    <div class="promo" role="img" aria-label="Snow-capped mountain under a blue sky"><b>Best Temple Tour of the Northern Hills</b><span>Click here for details</span></div>
  </section>
  <section class="side-block" style="border-bottom:0">
    <h2>OUR SHOP</h2>
  </section>
</aside>

<footer class="panel site-footer">
  <div class="footer-brand"><span class="brand-dot"></span><span class="brand-name">Bluewater Getaways KT</span></div>
  <div class="legal">COPYRIGHT 2013. ALL RIGHTS RESERVED.<br><a href="#">TERMS &amp; CONDITIONS</a> &nbsp;-&nbsp; <a href="#">PRIVACY</a> &nbsp;-&nbsp; <a href="#">DISCLAIMER</a></div>
  <div class="footer-art" role="img" aria-label="Bright orange and yellow flower artwork"></div>
</footer>
</body>
</html>
```